Your Harbor Agent Website Design

Creative Brief: Website Design for Your Harbor Agent
- Project Overview: Design a website for our new brand, "Your Harbor Agent". Your Harbor Agent is a service that matches clients with the perfect realtor. The primary function of this site is to serve as a lead generation hub, to generate leads of people who are looking to either buy or sell their house and need a great realtor. The site needs to have a very clean, modern design using sites like Tallyquest, Brickwell, Lantern, and Vexomill as an example. The site also needs to have a primary lead capture capability through a multi-step form or questionnaire that indicates if they are buying or selling, and depending on that selection, creates two different flows.

Target Audience:
- Homebuyers and sellers in the Denver area
- Individuals looking for high-quality realtor services
- Users seeking a seamless and professional online & home buying/selling experience

Objectives:
- Create a visually appealing, modern website with a strong emphasis on lead generation.
- Design advanced, multi-step forms for efficient lead capture.
- Ensure the website is user-friendly and optimized for both desktop and mobile devices.

Pages to Design:
Home Page:
- Engaging hero section with a clear call to action and the ability to enter the form flow
- Brief introduction to Your Harbor Agent and its unique value proposition
- Key features & benefits of being matched with a realtor by Your Harbor Agent
- Testimonials and success stories
- Lead capture form

About Page:
- Overview of Your Harbor Agent’s mission and values
- Professional and trust-building imagery

How it Works Page:
- Step-by-step explanation of the matching process (complete the form and we will match you with a realtor)
- Visual aids (icons, graphics) to simplify complex information
- Customer journey map from inquiry to successful match & sale of home
- Lead capture form

Contact Us Page:
- Simple and accessible contact form
- Contact details
- Call to action for immediate inquiries

Blog Template:
- Clean, easy-to-read layout for blog posts, primarily location/neighborhood guides as well as standard blogs
- Sidebar for recent posts, categories, and tags
- Social sharing buttons
- Lead capture form embedded within blog posts

Design Style:
- Modern and professional with a focus on usability
- Clean lines and intuitive navigation
- Use of curved corners and minimal straight lines for a sleek look
- Incorporation of graphic design elements, potentially including 3D and isomorphic design
- Inspired by sites like Tallyquest, Brickwell, Lantern, and Vexomill
Consistent color scheme and typography

Visual References:
- Tallyquest: For its professional and corporate look
- Brickwell and Lantern: For their user-friendly interfaces and modern design
- Vexomill: For its clean and functional layout

Target Market(s)

- Homebuyers and sellers in the Denver area, Individuals looking for high-quality realtor services, Users seeking a seamless and professional home buying/selling experience

Industry/Entity Type

Real Estate

Number of Pages Required

5+ page

Requirements
Must have
• Fully designed website with lead capture functionality based on brief
Nice to have
• Designed in Figma, Starting / Placeholder copy

```html
<!DOCTYPE html>
<html lang="en">
<head>
<meta charset="utf-8">
<title>Your Harbor Agent</title>
<link rel="stylesheet" href="https://fonts.googleapis.com/css2?family=Outfit:wght@300;400;500;600&family=Lora:wght@500;600&display=swap">
<style>
:root{
  --coral:#ee6352;
  --coral-soft:#f4a59a;
  --pink:#f9d3cc;
  --cream:#fbf3e6;
  --cream-light:#fcf4ea;
  --blush:#fdf3f0;
  --sand:#f2cc8c;
  --gold:#c9954a;
  --ink:#3b2712;
  --ink-soft:#6d5841;
  --footer:#2b1d0e;
  --white:#ffffff;
}
*{box-sizing:border-box;margin:0;padding:0}
html,body{width:1200px;height:4373px;overflow:hidden}
body{font-family:"Outfit",sans-serif;color:var(--ink);background:var(--cream);position:relative}
.abs{position:absolute}
section,header,footer{position:absolute;left:0;width:1200px}
.brand{font-family:"Lora",serif;font-weight:600;color:var(--coral);font-size:18px}

/* nav */
.site-nav{top:0;height:60px;background:var(--white)}
.site-nav .brand{left:53px;top:18px}
.nav-links{right:53px;top:13px;display:flex;align-items:center;gap:26px;font-size:13px;color:var(--ink)}
.btn-pill{background:var(--coral);color:var(--white);border-radius:20px;padding:9px 18px;font-size:13px;display:inline-block}

/* hero */
.hero{top:60px;height:680px;background:linear-gradient(180deg,#5b6b4a 0%,#6f5a3e 45%,#4c5a38 100%)}
.hero-title{top:226px;width:100%;text-align:center;color:var(--white);font-weight:500;font-size:48px;line-height:61px;letter-spacing:-.5px}
.search-tabs{left:212px;top:364px;display:flex;font-size:11px}
.search-tabs span{padding:6px 14px;background:var(--white);border-radius:6px 6px 0 0}
.search-tabs span.off{background:#e6e1da}
.search-bar{left:212px;top:391px;width:660px;height:65px;background:var(--white);border-radius:0 10px 10px 10px;display:flex;align-items:center;padding:0 14px}
.field{flex:1;padding:0 12px;border-right:1px solid #d8d2c9}
.field:last-of-type{border-right:none}
.field b{display:block;font-weight:500;font-size:11px;margin-bottom:6px}
.field i{font-size:10px;color:#9a8f82}
.search-bar .btn-pill{padding:8px 18px;font-size:11px}

/* intro */
.intro{top:740px;height:933px;background:var(--cream)}
.intro h2{top:96px;width:100%;text-align:center;font-weight:500;font-size:38px;line-height:48px}
.intro p.lead{left:322px;top:220px;width:556px;text-align:center;font-size:14px;line-height:22.5px;font-weight:300}
.intro .rule{left:277px;top:334px;width:646px;height:1px;background:#d9c7b0}
.featured{top:356px;width:100%;text-align:center;font-size:11px;letter-spacing:1.5px;color:var(--ink-soft)}
.press{top:396px;left:277px;width:646px;display:flex;justify-content:space-between;padding:0 0;font-weight:600;font-size:26px;color:var(--gold)}
.intro-art{left:389px;top:524px;width:746px;height:409px;border-radius:300px 300px 0 0;background:linear-gradient(180deg,var(--pink),var(--coral-soft) 70%,#eb9a8e)}

/* why */
.why{top:1673px;height:796px;background:var(--sand)}
.why-photo{left:51px;top:138px;width:560px;height:516px;border-radius:14px;background:linear-gradient(135deg,#d7ccbc,#9fb2b7 55%,#7e8c7a)}
.review-card{left:98px;top:94px;width:277px;height:103px;background:rgba(251,243,230,.85);border-radius:14px;padding:16px 20px 0 120px;font-size:13px}
.review-card .avatar{left:36px;top:18px;width:66px;height:66px;border-radius:50%;background:#c8b6a0}
.review-card b{font-weight:500;display:block}
.stars{color:#f0b429;font-size:20px;letter-spacing:2px}
.stat-card{left:377px;top:592px;width:300px;height:108px;background:rgba(251,243,230,.9);border-radius:14px}
.stat-card .ic{left:36px;top:28px;width:52px;height:52px;border-radius:50%;background:var(--white)}
.stat-card strong{position:absolute;left:130px;top:26px;font-size:32px;font-weight:500}
.stat-card span{position:absolute;left:130px;top:66px;font-size:14px}
.why h2{left:713px;top:150px;font-size:38px;font-weight:500}
.feature{left:711px;width:440px}
.feature .ic{position:absolute;left:0;top:0;width:48px;height:48px;border-radius:10px;background:var(--cream);display:flex;align-items:center;justify-content:center}
.feature h3{margin-left:68px;font-size:19px;font-weight:500;line-height:24px}
.feature p{margin-left:68px;margin-top:14px;font-size:12.5px;line-height:20px;font-weight:300}

/* stories */
.stories{top:2469px;height:667px;background:var(--cream-light)}
.stories h2{left:49px;top:94px;font-size:38px;font-weight:500}
.stories .sub{left:49px;top:165px;font-size:14px;font-weight:300}
.story{top:251px;width:350px;height:255px;border:1px solid var(--gold);border-radius:14px;padding:28px 26px;font-size:14px;line-height:22.5px;font-weight:300}
.story .who{position:absolute;left:26px;bottom:28px;display:flex;align-items:center;gap:20px;font-size:12.5px;line-height:18px}
.story .who i{width:44px;height:44px;border-radius:50%;background:#c9ae93;display:block}
.story .who b{font-weight:500;display:block}
.story .who em{font-style:normal;color:var(--gold)}
.dots{left:49px;top:551px;display:flex;gap:6px}
.dots i{width:5px;height:5px;border-radius:50%;background:var(--ink)}
.arrow{top:533px;width:40px;height:40px;border:1.5px solid var(--gold);border-radius:50%;display:flex;align-items:center;justify-content:center}

/* cta */
.cta{top:3136px;height:270px;background:var(--coral);color:var(--white);text-align:center}
.cta h2{top:70px;width:100%;font-size:40px;font-weight:500}
.cta p{left:330px;top:140px;width:540px;font-size:14px;line-height:22.5px;font-weight:300}

/* lead form */
.lead-form{top:3406px;height:511px;background:var(--blush)}
.form-art{left:51px;top:158px;width:526px;height:353px;border-radius:260px 260px 0 0;background:linear-gradient(180deg,var(--pink),#f3b6ad 75%,var(--coral-soft))}
.step{left:694px;top:141px;font-size:12px;color:#b3a595}
.question{left:694px;top:220px;font-size:19px;font-weight:500}
.choice{left:691px;width:341px;height:46px;border:2px solid var(--coral);border-radius:8px;background:var(--white);color:var(--coral);font-size:15px;font-weight:500;display:flex;align-items:center;justify-content:center}
.next{left:930px;top:426px;width:100px;height:41px;border-radius:21px;background:var(--coral);color:var(--white);font-size:13px;display:flex;align-items:center;justify-content:center;gap:12px}

/* footer */
.site-footer{top:3917px;height:456px;background:var(--footer);color:var(--white)}
.site-footer .brand{left:53px;top:72px;color:var(--white);font-size:19px}
.foot-col h4{font-size:12.5px;font-weight:500;margin-bottom:22px}
.foot-col a{display:block;font-size:11px;color:var(--white);text-decoration:none;margin-bottom:17px}
.subscribe{left:730px;top:74px;width:418px}
.subscribe p{font-size:12px;margin-bottom:18px;font-weight:300}
.subscribe .row{display:flex;gap:12px}
.subscribe .input{width:305px;height:40px;border-radius:8px;background:var(--white);color:#9a8f82;font-size:12px;padding:12px 12px}
.subscribe .btn{width:100px;height:40px;border-radius:20px;border:1.5px solid var(--white);font-size:12px;display:flex;align-items:center;justify-content:center}
.subscribe small{display:block;font-size:9px;line-height:13px;margin-top:12px;font-weight:300}
.foot-rule{left:53px;top:341px;width:1094px;height:1px;background:#6b5a48}
.legal{left:53px;top:370px;display:flex;gap:22px;font-size:10.5px;font-weight:300}
.legal u{text-underline-offset:2px}
.social{right:53px;top:368px;display:flex;gap:14px}
.social i{width:16px;height:16px;border-radius:50%;background:var(--white);display:block}
</style>
</head>
<body>

<header class="site-nav">
  <div class="brand abs">Your Harbor Agent</div>
  <nav class="nav-links abs"><span>About Us</span><span>How it Works</span><span>Blog</span><span class="btn-pill" style="margin-left:6px">Contact Us</span></nav>
</header>

<section class="hero" role="img" aria-label="Photo of a timber lodge-style home beside a lake surrounded by trees">
  <h1 class="hero-title abs">Your Harbor Agent:<br>Your Perfect Match in Real Estate</h1>
  <div class="search-tabs abs"><span>Buy</span><span class="off">Sell</span></div>
  <div class="search-bar abs">
    <div class="field"><b>Property Type</b><i style="font-style:normal">Select Property Type &#8964;</i></div>
    <div class="field"><b>Location</b><i>eg. Littleton, Belmar</i></div>
    <div class="field"><b>Price Range</b><i>Min. Price-Max. Price</i></div>
    <span class="btn-pill">Search</span>
  </div>
</section>

<section class="intro">
  <h2 class="abs">Making Real Estate Connections<br>Easy and Effective!</h2>
  <p class="lead abs">At Your Harbor Agent, we understand that finding the right realtor can make all the difference in your real estate journey. Whether you're looking to buy your dream home or sell your property for the best price, our mission is to connect you with the perfect realtor who understands your unique needs and goals.</p>
  <div class="rule abs"></div>
  <div class="featured abs">FEATURED IN</div>
  <div class="press abs"><span>Meridian</span><span>Ledger Daily</span><span>Capstone</span></div>
  <div class="intro-art abs" role="img" aria-label="Flat illustration of pink and coral townhouses, a tall white building and small trees"></div>
</section>

<section class="why">
  <div class="why-photo abs" role="img" aria-label="Photo of a smiling couple shaking hands with a realtor while receiving house keys"></div>
  <div class="review-card abs">
    <i class="avatar abs" role="img" aria-label="Reviewer portrait"></i>
    <b>Arnold B.</b>Summit Key Realty
    <div class="stars">★★★★★</div>
  </div>
  <div class="stat-card abs">
    <i class="ic abs" role="img" aria-label="Small house illustration"></i>
    <strong>315</strong><span>Homes sold in Denver</span>
  </div>
  <h2 class="abs">Why Choose Us?</h2>
  <div class="feature abs" style="top:241px">
    <span class="ic"><svg width="22" height="22" viewBox="0 0 24 24" fill="none" stroke="#c9954a" stroke-width="1.6"><circle cx="7" cy="6" r="2.5"/><circle cx="17" cy="6" r="2.5"/><path d="M4 20v-7a3 3 0 0 1 6 0v7M14 20v-7a3 3 0 0 1 6 0v7"/></svg></span>
    <h3>Tailored Matches</h3>
    <p>We take the time to understand your specific requirements and preferences, ensuring that we match you with a realtor who specializes in your desired neighborhood, property type, and budget.</p>
  </div>
  <div class="feature abs" style="top:391px">
    <span class="ic"><svg width="22" height="22" viewBox="0 0 24 24" fill="none" stroke="#c9954a" stroke-width="1.6"><path d="M7 4h10v5a5 5 0 0 1-10 0z"/><path d="M7 6H4a3 3 0 0 0 3 4M17 6h3a3 3 0 0 1-3 4M12 14v4M8 20h8"/></svg></span>
    <h3>Experienced Professionals</h3>
    <p>Our network of realtors consists of top-rated professionals with extensive knowledge of the Denver real estate market. They are dedicated to providing exceptional service and achieving the best outcomes for their clients.</p>
  </div>
  <div class="feature abs" style="top:538px">
    <span class="ic"><svg width="22" height="22" viewBox="0 0 24 24" fill="none" stroke="#c9954a" stroke-width="1.6"><circle cx="6" cy="5" r="2.5"/><circle cx="6" cy="19" r="2.5"/><rect x="13" y="10" width="7" height="4" rx="1"/><path d="M6 8v8M6 12h7"/></svg></span>
    <h3>Streamlined Process</h3>
    <p>Say goodbye to the hassle of searching for a realtor on your own. Our streamlined process makes it easy and stress-free to find the perfect match, so you can focus on what matters most – your next move.</p>
  </div>
</section>

<section class="stories">
  <h2 class="abs">Success Stories</h2>
  <p class="sub abs">Listen to the experience of our happy clients.</p>
  <article class="story abs" style="left:49px">"Working with Your Harbor Agent was a game-changer. They connected us with a fantastic realtor who helped us sell our home quickly and for a great price. The process was smooth and stress-free!"
    <div class="who"><i></i><div><b>Sarah and John M.</b><em>Satisfied Clients</em></div></div></article>
  <article class="story abs" style="left:425px">"As first-time homebuyers, we were nervous about the process, but Your Harbor Agent made it so easy. They matched us with an experienced realtor who guided us every step of the way."
    <div class="who"><i></i><div><b>Emily R.</b><em>Happy Homeowner</em></div></div></article>
  <article class="story abs" style="left:801px">"I had a tight deadline to sell my house and move for a new job. Your Harbor Agent matched me with a realtor who was incredibly efficient and effective. My house sold in record time, and I couldn't be happier with the service."
    <div class="who"><i></i><div><b>Michael T.</b><em>Relocated Professional</em></div></div></article>
  <article class="story abs" style="left:1179px"></article>
  <div class="dots abs"><i></i><i></i><i></i><i></i><i></i></div>
  <div class="arrow abs" style="left:1049px"><svg width="14" height="14" viewBox="0 0 24 24" fill="none" stroke="#3b2712" stroke-width="2"><path d="M20 12H4M10 6l-6 6 6 6"/></svg></div>
  <div class="arrow abs" style="left:1101px"><svg width="14" height="14" viewBox="0 0 24 24" fill="none" stroke="#3b2712" stroke-width="2"><path d="M4 12h16M14 6l6 6-6 6"/></svg></div>
</section>

<section class="cta">
  <h2 class="abs">Get Started Today!</h2>
  <p class="abs">Ready to find the perfect realtor for your real estate journey? Fill out the form today and let Your Harbor Agent connect you with the best professional to meet your needs. Your dream home or ideal sale is just a click away!</p>
</section>

<section class="lead-form">
  <div class="form-art abs" role="img" aria-label="Flat illustration of a pink house, a small cottage and round trees"></div>
  <div class="step abs">Step 1 of 13</div>
  <div class="question abs">Are you looking to buy or sell a home?</div>
  <div class="choice abs" style="top:278px">Buy a home</div>
  <div class="choice abs" style="top:348px">Sell a home</div>
  <div class="next abs">Next <svg width="12" height="12" viewBox="0 0 24 24" fill="none" stroke="#fff" stroke-width="2.4"><path d="M4 12h16M14 6l6 6-6 6"/></svg></div>
</section>

<footer class="site-footer">
  <div class="brand abs">Your Harbor Agent</div>
  <div class="foot-col abs" style="left:355px;top:74px">
    <h4>Quick Links</h4>
    <a>About Us</a><a>How it Works</a><a>Blog</a><a>Contact Us</a>
  </div>
  <div class="subscribe abs foot-col">
    <h4 style="margin-bottom:16px">Subscribe</h4>
    <p>Join our newsletter to stay up to date on features and releases.</p>
    <div class="row"><div class="input">Enter your email</div><div class="btn">Subscribe</div></div>
    <small>By subscribing you agree to with our <u>Privacy Policy</u> and provide consent to receive updates from our company.</small>
  </div>
  <div class="foot-rule abs"></div>
  <div class="legal abs"><span>© 2024 Your Harbor Agent. All rights reserved.</span><u>Privacy Policy</u><u>Terms of Service</u><u>Cookies Settings</u></div>
  <div class="social abs" aria-label="Social links"><i></i><i></i><i></i><i></i><i></i></div>
</footer>

</body>
</html>
```